Business Card Design

We need a business card design for a new company called Riverbend Advisory, LLC. We are a project management and software engineering consulting company. We prefer to use blues but am open to any colors. We would like out design to show strength and creativity.

I've uploaded new logo designs to the project.  Please use these logo designs for the business card. Thanks!

Industry/Entity Type

Software

Contact Information for Business Card

Daniel Whitford
Consultant
Owner

Riverbend Advisory, LLC

2716 5th St. S #4372
Arlington, VA 22198

703-555-0187
dwhitford@rvbadv.example
www.rvbadv.example

```html
<!DOCTYPE html>
<html lang="en">
<head>
<meta charset="utf-8">
<title>Riverbend Advisory – Business Card</title>
<link href="https://fonts.googleapis.com/css2?family=Open+Sans:wght@400;600;700&display=swap" rel="stylesheet">
<style>
  :root {
    --navy: #1d3a5c;
    --navy-deep: #0f3352;
    --orange: #e0792a;
    --orange-bright: #ea6a24;
    --paper: #f4f4f4;
    --stage: #e9eaec;
    --white: #ffffff;
  }
  * { margin: 0; padding: 0; box-sizing: border-box; }
  html, body { width: 1200px; height: 1000px; overflow: hidden; }
  body {
    background: var(--stage);
    font-family: "Open Sans", Arial, sans-serif;
    position: relative;
  }
  .card {
    position: absolute;
    left: 250px;
    width: 700px;
    height: 400px;
    border-radius: 4px;
    box-shadow: 0 10px 30px rgba(0,0,0,0.18);
    overflow: hidden;
  }
  /* Front */
  .card-front {
    top: 60px;
    background: linear-gradient(160deg, var(--white) 0%, var(--paper) 100%);
    color: var(--navy);
  }
  .front-brand {
    position: absolute;
    left: 48px;
    top: 52px;
    font-size: 30px;
    font-weight: 600;
    letter-spacing: -0.5px;
    color: var(--navy);
    text-transform: uppercase;
  }
  .company-address {
    position: absolute;
    right: 48px;
    top: 56px;
    text-align: right;
    font-size: 15px;
    font-weight: 700;
    line-height: 1.35;
    color: var(--navy);
  }
  .contact {
    position: absolute;
    left: 48px;
    top: 190px;
  }
  .contact-name {
    font-size: 34px;
    font-weight: 600;
    color: var(--navy);
    line-height: 1.1;
  }
  .contact-title {
    font-size: 19px;
    color: var(--orange);
    margin-bottom: 18px;
  }
  .contact-line {
    font-size: 16px;
    color: var(--navy);
    line-height: 1.6;
  }
  .contact-line .label {
    color: var(--orange);
    font-weight: 700;
  }
  .website {
    position: absolute;
    right: 48px;
    bottom: 40px;
    font-size: 20px;
    font-weight: 600;
    color: var(--navy);
  }
  /* Back */
  .card-back {
    top: 540px;
    background: linear-gradient(200deg, var(--navy-deep) 0%, var(--navy-deep) 45%, #5a4a45 68%, var(--orange-bright) 100%);
    display: flex;
    align-items: center;
    justify-content: center;
  }
  .back-brand {
    display: flex;
    align-items: center;
    gap: 18px;
    color: var(--white);
    font-size: 44px;
    font-weight: 400;
    letter-spacing: 1px;
    text-transform: uppercase;
  }
  .back-brand .mark {
    width: 22px;
    height: 22px;
    background: var(--white);
  }
</style>
</head>
<body>
  <section class="card card-front" aria-label="Business card front">
    <div class="front-brand">Riverbend Advisory</div>
    <address class="company-address" style="font-style:normal">
      Riverbend Advisory, LLC<br>
      2716 5th St. S #4372<br>
      Arlington, VA 22198
    </address>
    <div class="contact">
      <div class="contact-name">Daniel Whitford</div>
      <div class="contact-title">Consultant Owner</div>
      <div class="contact-line"><span class="label">phone:</span> 703-555-0187</div>
      <div class="contact-line"><span class="label">email:</span> dwhitford@rvbadv.example</div>
    </div>
    <div class="website">www.rvbadv.example</div>
  </section>

  <section class="card card-back" aria-label="Business card back">
    <div class="back-brand"><span class="mark"></span>Riverbend Advisory</div>
  </section>
</body>
</html>
```